Postcard Design

BRT Ltd are a screen and large format digital company that specialise is direct to substrate marketing. I would like a postcard design to send to clients with every job we send out, informing them of other items we can do.
From conventional screen printing to digital printing from vehicle graphics to glass printing, from exhibition panels to window graphics, banners etc.
You can read more on our web site www.brt-ltd-example.com
Emphasis on dealing directly with the printers instead of using a middle marketing company
we like the back to be a reply card , with the logo but like the idea or the paper looking scrunched up as in the pixel hive advert.
hi re logo to be used as supplied

Target Market(s)

Other printers who we trade print for and Marketing agencies

Industry/Entity Type

Screen Printing

Requirements
Must have
• Company logo
Nice to have
• Something different.......BE BOLD, almost quirky
Should not have
• the usual Printers CMYK cack

```html
<!DOCTYPE html>
<html lang="en">
<head>
<meta charset="utf-8">
<title>BRT Ltd Postcard</title>
<link rel="stylesheet" href="https://fonts.googleapis.com/css2?family=Tinos:wght@400;700&family=Arimo:wght@400;700&display=swap">
<style>
  :root {
    --page: #ecebe8;
    --navy: #0f1626;
    --navy-rule: #c9ccd6;
    --reply-grey: #dcdde3;
    --ink: #1b1b1b;
    --white: #ffffff;
    --cream: #f3efc4;
    --panel: rgba(40, 40, 44, 0.72);
    --band: #151515;
    --teal: #3f9fa8;
    --green: #9cc64a;
    --orange: #e59a2c;
    --photo-light: #e6e3dd;
    --photo-mid: #c9c4bb;
  }
  * { box-sizing: border-box; margin: 0; padding: 0; }
  html, body { width: 1200px; height: 900px; overflow: hidden; }
  body {
    background: var(--page);
    font-family: "Tinos", "Times New Roman", serif;
    position: relative;
  }
  .postcard {
    position: absolute;
    left: 290px;
    width: 620px;
    height: 413px;
    overflow: hidden;
    box-shadow: 0 6px 18px rgba(0,0,0,0.18);
  }
  .postcard--reply { top: 22px; display: flex; }
  .postcard--front { top: 465px; }

  /* Reply side */
  .reply-info {
    width: 50%;
    background: var(--navy);
    color: var(--white);
    padding: 26px 20px 0 22px;
    position: relative;
  }
  .brand-lockup {
    display: flex;
    align-items: center;
    gap: 12px;
    margin: 10px 0 0 42px;
    height: 108px;
  }
  .brand-lockup__dot {
    width: 56px; height: 56px;
    border-radius: 50%;
    background: var(--cream);
  }
  .brand-lockup__name {
    font-family: "Arimo", Arial, sans-serif;
    font-weight: 700;
    font-size: 34px;
    color: var(--white);
  }
  .reply-info__tagline {
    font-weight: 700;
    font-size: 15px;
    text-align: center;
    margin-top: 4px;
  }
  .reply-info__services {
    font-size: 7.5px;
    font-weight: 700;
    text-align: center;
    margin-top: 4px;
  }
  .reply-info__prompt {
    font-size: 11.5px;
    font-weight: 700;
    text-align: center;
    margin-top: 6px;
    padding-bottom: 8px;
    border-bottom: 2px solid var(--navy-rule);
    margin-left: -22px;
    margin-right: -20px;
  }
  .reply-info__company {
    font-size: 19px;
    font-weight: 700;
    text-align: center;
    margin: 12px 0 12px;
  }
  .contact-list { list-style: none; }
  .contact-list li {
    display: flex;
    align-items: center;
    gap: 14px;
    font-size: 11.5px;
    font-weight: 700;
    height: 25px;
  }
  .contact-list svg { width: 18px; height: 18px; flex: none; }

  .reply-address {
    width: 50%;
    background: var(--reply-grey);
    position: relative;
    border-left: 2px solid var(--white);
  }
  .reply-address__divider {
    position: absolute; left: 8px; top: 0; bottom: 0;
    width: 2px; background: var(--ink);
  }
  .reply-address__stamp {
    position: absolute; right: 28px; top: 24px;
    width: 64px; height: 78px;
    border: 2px solid var(--ink);
  }
  .reply-address__line {
    position: absolute; left: 28px; right: 22px;
    border-top: 1px dotted #555;
  }

  /* Front side */
  .front-photo {
    position: absolute; inset: 0;
    background: linear-gradient(100deg, var(--photo-mid) 0%, var(--photo-light) 45%, #d8d2c6 100%);
  }
  .front-stripes {
    position: absolute; left: 18px; top: 0; bottom: 0; width: 40px;
    background: linear-gradient(90deg, var(--teal) 0 30%, #6fb7a2 30% 55%, var(--green) 55% 100%);
  }
  .front-stripes--right {
    left: auto; right: 30px; width: 26px;
    background: linear-gradient(90deg, var(--green) 0 50%, var(--orange) 50% 100%);
  }
  .front-panel {
    position: absolute; left: 62px; top: 0; width: 170px; bottom: 0;
    background: var(--panel);
    color: var(--white);
    padding-top: 22px;
  }
  .front-panel .brand-lockup { margin: 0 0 0 32px; height: 64px; gap: 8px; }
  .front-panel .brand-lockup__dot { width: 34px; height: 34px; }
  .front-panel .brand-lockup__name { font-size: 22px; }
  .front-panel__lead {
    font-family: "Arimo", Arial, sans-serif;
    font-size: 12px; margin: 20px 0 0 18px;
  }
  .front-panel__headline {
    font-weight: 700; font-size: 23px; line-height: 1.15;
    margin: 4px 0 0 18px; letter-spacing: 0.5px;
  }
  .front-panel__company {
    font-family: "Arimo", Arial, sans-serif;
    font-size: 24px; margin: 12px 0 0 20px;
  }
  .front-panel__promise {
    font-family: "Arimo", Arial, sans-serif;
    font-size: 11px; text-align: right; padding-right: 22px;
  }
  .front-email {
    position: absolute; left: 0; top: 262px; width: 232px; height: 40px;
    background: var(--band);
    color: var(--white);
    font-family: "Arimo", Arial, sans-serif;
    font-size: 12.5px;
    padding: 12px 0 0 70px;
  }
  .front-footer {
    position: absolute; left: 0; right: 0; bottom: 0; height: 105px;
  }
  .front-footer__call {
    position: absolute; left: 232px; top: 0; width: 200px; height: 34px;
    background: var(--band); color: var(--white);
    font-family: "Arimo", Arial, sans-serif; font-weight: 700; font-size: 13px;
    padding: 10px 0 0 14px;
  }
  .front-footer__address {
    position: absolute; left: 232px; top: 44px;
    font-weight: 700; font-size: 14px; color: var(--ink); letter-spacing: 0.6px;
  }
  .front-footer__web {
    position: absolute; left: 0; right: 0; bottom: 0; height: 34px;
    background: var(--band); color: var(--white);
    font-family: "Arimo", Arial, sans-serif; font-size: 13px;
    text-align: right; padding: 9px 64px 0 0;
  }
</style>
</head>
<body>

<section class="postcard postcard--reply" aria-label="Reply side of postcard">
  <div class="reply-info">
    <div class="brand-lockup">
      <span class="brand-lockup__dot"></span>
      <span class="brand-lockup__name">BRT Ltd</span>
    </div>
    <p class="reply-info__tagline">The Latest In Digital Print Technology</p>
    <p class="reply-info__services">Retail Graphics | Vehicle Graphics | Interior Graphics | Banners | Posters | Glass Printing</p>
    <p class="reply-info__prompt">For more information contact:</p>
    <h2 class="reply-info__company">BRT Limited</h2>
    <ul class="contact-list">
      <li>
        <svg viewBox="0 0 18 18"><rect x="5" y="1" width="8" height="16" rx="1.5" fill="none" stroke="#fff" stroke-width="1.6"/><line x1="7.5" y1="14.5" x2="10.5" y2="14.5" stroke="#fff" stroke-width="1.4"/></svg>
        020 7946 0321
      </li>
      <li>
        <svg viewBox="0 0 18 18"><text x="9" y="14" text-anchor="middle" font-family="Arimo, Arial, sans-serif" font-size="16" font-weight="700" fill="#fff">@</text></svg>
        info@brt-ltd-example.com
      </li>
      <li>
        <svg viewBox="0 0 18 18"><rect x="1" y="2" width="16" height="11" rx="1" fill="none" stroke="#fff" stroke-width="1.8"/><rect x="6" y="14" width="6" height="2" fill="#fff"/></svg>
        www.brt-ltd-example.com
      </li>
      <li>
        <svg viewBox="0 0 18 18"><path d="M9 1 L17 9 H14.5 V17 H11 V12 H7 V17 H3.5 V9 H1 Z" fill="#fff"/></svg>
        14 Harbour Lane, Kingsford, Surrey, KT9 2ZX
      </li>
    </ul>
  </div>
  <div class="reply-address">
    <span class="reply-address__divider"></span>
    <span class="reply-address__stamp"></span>
    <span class="reply-address__line" style="top:170px"></span>
    <span class="reply-address__line" style="top:215px"></span>
    <span class="reply-address__line" style="top:260px"></span>
    <span class="reply-address__line" style="top:305px"></span>
  </div>
</section>

<section class="postcard postcard--front" aria-label="Front side of postcard">
  <div class="front-photo" role="img" aria-label="Photograph of glass panels printed with goldfish swimming"></div>
  <span class="front-stripes"></span>
  <span class="front-stripes front-stripes--right"></span>
  <div class="front-panel">
    <div class="brand-lockup">
      <span class="brand-lockup__dot"></span>
      <span class="brand-lockup__name">BRT Ltd</span>
    </div>
    <p class="front-panel__lead">Looking for a</p>
    <h1 class="front-panel__headline">DIGITAL<br>PRINTING?</h1>
    <p class="front-panel__company">BRT Ltd</p>
    <p class="front-panel__promise">Will Help U!</p>
  </div>
  <div class="front-email">info@brt-ltd-example.com</div>
  <div class="front-footer">
    <div class="front-footer__call">Call:020 7946 0321</div>
    <p class="front-footer__address">14 Harbour Lane, Kingsford, Surrey, KT9 2ZX</p>
    <div class="front-footer__web">www.northpeak-studio.com</div>
  </div>
</section>

</body>
</html>
```